Basic Letterhead Design

We need a Letterhead design. Our company is in the financial services industry. We are a small bank who lends money. I have uploaded an example our current letterhead design. We would like a new one.

```html
<!DOCTYPE html>
<html lang="en">
<head>
<meta charset="utf-8">
<title>Harlow Lending Letterhead</title>
<link href="https://fonts.googleapis.com/css2?family=Arimo:wght@400&family=Work+Sans:wght@500&display=swap" rel="stylesheet">
<style>
  :root {
    --forest: #214634;
    --ink: #3a3a3a;
    --paper: #f4f4f3;
    --backdrop: #e6e6e6;
    --white: #ffffff;
    --sig: #1f2530;
  }
  * { box-sizing: border-box; margin: 0; padding: 0; }
  html, body {
    width: 1176px; height: 1200px; overflow: hidden;
    background: var(--backdrop);
  }
  .letterhead {
    position: absolute; left: 192px; top: 40px;
    width: 792px; height: 1120px;
    background: var(--paper);
    font-family: "Arimo", Arial, sans-serif;
    color: var(--ink);
  }
  .brand {
    position: absolute; left: 56px; top: 84px;
    display: flex; align-items: center; gap: 10px;
    font-family: "Work Sans", Arial, sans-serif;
    font-weight: 500; font-size: 22px; letter-spacing: 1px;
    color: var(--forest);
  }
  .brand-dot {
    width: 18px; height: 18px; border-radius: 50%;
    background: var(--forest);
  }
  .address-band {
    position: absolute; left: 300px; right: 0; top: 88px; height: 50px;
    background: var(--forest);
    display: flex; align-items: center; justify-content: center;
    font-family: "Work Sans", Arial, sans-serif;
    font-weight: 500; font-size: 14px; letter-spacing: 0.6px;
    color: var(--white);
  }
  .letter {
    position: absolute; left: 96px; right: 96px; top: 206px;
  }
  .salutation { font-size: 19px; margin-bottom: 30px; }
  .letter p {
    font-size: 12px; line-height: 1.6; margin-bottom: 14px;
  }
  .closing { font-size: 12px; margin-top: 34px; }
  .signature {
    display: block; margin-top: 22px;
    width: 130px; height: 44px;
  }
  .acn {
    position: absolute; left: 0; right: 0; bottom: 70px;
    text-align: center;
    font-family: "Work Sans", Arial, sans-serif;
    font-weight: 500; font-size: 16px; letter-spacing: 1px;
    color: var(--forest);
  }
</style>
</head>
<body>
  <main class="letterhead">
    <header>
      <div class="brand"><span class="brand-dot"></span>HARLOW LENDING</div>
      <div class="address-band">Harlow Lending Pty Ltd, 42 Banksia St, Greenvale Nsw 2190</div>
    </header>

    <section class="letter">
      <h1 class="salutation" style="font-weight:400">Dear Mr. Carter,</h1>
      <p>Lorem ipsum dolor sit amet, consectetur adipiscing elit. Donec orci purus, luctus vitae dignissim eu, iaculis sed purus. Vivamus faucibus, ipsum nec aliquet viverra, leo mauris condimentum ligula, sit amet sagittis enim ligula quis arcu. Nam egestas tortor id nisi porttitor mattis. In tortor ante, ultricies in suscipit a, tempus non massa. Vivamus et auctor mi. Fusce vel massa nulla. Phasellus nec eros mauris, et scelerisque orci.</p>
      <p>Donec malesuada orci vitae nulla accumsan porta a id massa. Quisque accumsan iaculis magna sit amet fringilla. Maecenas consequat, magna eget tincidunt semper, odio nibh rutrum mi, id feugiat ante nisi eu risus. Vestibulum nunc orci, rhoncus a placerat in, ultricies in mi. Cras mattis varius eros, vel fringilla nisi suscipit eget. Quisque scelerisque sagittis nulla at porttitor.</p>
      <p>Sed id augue vitae urna euismod commodo aliquet a quam. Pellentesque arcu velit, cursus et malesuada ut, consequat et diam. Nullam erat sem, rhoncus id ullamcorper vitae, rhoncus et arcu. In ultricies ultricies nulla, ut rutrum nisi iaculis at. Donec eu magna a metus ornare faucibus. Fusce aliquet faucibus ultricies. Morbi semper, est id tincidunt gravida, sem arcu adipiscing lacus, ac bibendum nulla leo eu purus. Quisque nec diam sed risus consectetur a ccumsan quis quis nibh. Vestibulum id purus lorem.</p>
      <p>It is a long established fact that a reader will be distracted by the readable content of a page when looking at its layout. The point of using Lorem Ipsum is that it has a more-or-less normal distribution of letters, as opposed to using 'Content here, content here', making it look like readable English. Many desktop publishing packages</p>
      <p>ada ut, consequat et diam. Nullam erat sem, rhoncus id ullamcorper vitae, rhoncus et arcu. In ultricies ultricies nulla, ut rutrum nisi iaculis at. Donec eu magna a metus ornare faucibus. Fusce aliquet faucibus ultricies. Morbi semper,</p>
      <div class="closing">Sincerely,</div>
      <svg class="signature" role="img" aria-label="Handwritten signature of the sender" viewBox="0 0 130 44">
        <rect x="0" y="14" width="130" height="16" rx="8" fill="var(--sig)" opacity="0.18"/>
      </svg>
    </section>

    <footer class="acn">ACN: 512 380 967</footer>
  </main>
</body>
</html>
```